KerrLow Farm

Need a nice simple clean double sided business card that has our logo and info on:
Kerr Low Farm
Martin & Felicity Kerr Low
kerrlowfarm@mailbarn.example
Martin: 1-780-555-0148
Felicity: 1-780-555-0193
Instagram @ kerrlow_farm

Contact Information for Business Card

Martin & Felicity Kerr Low kerrlowfarm@mailbarn.example Martin: 1-780-555-0148 Felicity: 1-780-555-0193

```html
<!DOCTYPE html>
<html lang="en">
<head>
<meta charset="utf-8">
<title>Kerr Low Farm — Business Card</title>
<link rel="stylesheet" href="https://fonts.googleapis.com/css2?family=EB+Garamond:wght@500&family=Open+Sans:ital,wght@0,400;1,400&display=swap">
<style>
  :root {
    --canvas: #e4e4e4;
    --card-white: #ffffff;
    --farm-green: #669e0f;
    --harvest-orange: #ffa200;
    --night: #1c1d1f;
    --ink-light: #ffffff;
    --serif: "EB Garamond", Georgia, serif;
    --sans: "Open Sans", Arial, sans-serif;
  }
  * { box-sizing: border-box; margin: 0; padding: 0; }
  html, body { width: 1200px; height: 800px; overflow: hidden; }
  body { background: var(--canvas); position: relative; font-family: var(--sans); }

  .card { position: absolute; border-radius: 26px; overflow: hidden; box-shadow: 0 14px 30px rgba(0,0,0,.18); }

  /* Front: contact side */
  .card-front { left: 110px; top: 90px; width: 370px; height: 620px; background: var(--card-white); }
  .front-art { position: absolute; inset: 0; }
  .wheat-art { position: absolute; left: 190px; top: 120px; width: 140px; height: 200px;
    border-radius: 70px 70px 20px 20px;
    background: linear-gradient(160deg, #ffc24d, #ffa200 55%, #7fb32a); opacity: .85; }
  .front-info { position: absolute; left: 34px; top: 372px; width: 300px; color: var(--ink-light); }
  .owner-names { font-family: var(--serif); font-weight: 500; font-size: 21px; line-height: 1.15;
    letter-spacing: .5px; text-transform: uppercase; text-align: center; margin-bottom: 22px; }
  .contact-list { list-style: none; display: flex; flex-direction: column; gap: 10px; }
  .contact-item { display: flex; align-items: center; gap: 10px; font-size: 13.5px; }
  .contact-item em { font-style: italic; opacity: .95; }
  .contact-icon { width: 26px; height: 26px; border-radius: 50%; background: var(--card-white);
    display: flex; align-items: center; justify-content: center; flex: none; }
  .contact-icon svg { width: 14px; height: 14px; }

  /* Back: brand side */
  .card-back { left: 530px; top: 210px; width: 600px; height: 370px; background: var(--night); }
  .brand { position: absolute; inset: 0; display: flex; flex-direction: column; align-items: center; justify-content: center; gap: 26px; }
  .brand-ring { width: 120px; height: 120px; border-radius: 50%; border: 4px solid var(--farm-green); }
  .brand-name { font-family: var(--serif); font-weight: 500; font-size: 46px; color: var(--farm-green);
    text-transform: uppercase; letter-spacing: 1px; }
</style>
</head>
<body>

<section class="card card-front" aria-label="Contact side">
  <svg class="front-art" viewBox="0 0 370 620" aria-hidden="true">
    <circle cx="120" cy="600" r="300" fill="none" stroke="var(--farm-green)" stroke-width="4"/>
    <circle cx="120" cy="600" r="294" fill="none" stroke="var(--harvest-orange)" stroke-width="6"/>
    <circle cx="120" cy="600" r="289" fill="var(--farm-green)"/>
  </svg>
  <div class="wheat-art" role="img" aria-label="Illustration of two golden wheat stalks with green leaves"></div>

  <div class="front-info">
    <h1 class="owner-names">Martin &amp;<br>Felicity Kerr Low</h1>
    <ul class="contact-list">
      <li class="contact-item">
        <span class="contact-icon"><svg viewBox="0 0 14 14"><rect x="3.5" y="1" width="7" height="12" rx="1.5" fill="none" stroke="var(--harvest-orange)" stroke-width="1.5"/><circle cx="7" cy="11" r=".8" fill="var(--harvest-orange)"/></svg></span>
        <span>1-780-555-0148 <em>Martin</em></span>
      </li>
      <li class="contact-item">
        <span class="contact-icon"><svg viewBox="0 0 14 14"><rect x="3.5" y="1" width="7" height="12" rx="1.5" fill="none" stroke="var(--harvest-orange)" stroke-width="1.5"/><circle cx="7" cy="11" r=".8" fill="var(--harvest-orange)"/></svg></span>
        <span>1-780-555-0193 <em>Felicity</em></span>
      </li>
      <li class="contact-item">
        <span class="contact-icon"><svg viewBox="0 0 14 14"><rect x="1.5" y="3" width="11" height="8" rx="1" fill="var(--harvest-orange)"/><path d="M1.5 3.5 7 8l5.5-4.5" fill="none" stroke="#fff" stroke-width="1"/></svg></span>
        <span>kerrlowfarm@mailbarn.example</span>
      </li>
      <li class="contact-item">
        <span class="contact-icon"><svg viewBox="0 0 14 14"><circle cx="7" cy="7" r="4.5" fill="none" stroke="var(--harvest-orange)" stroke-width="1.6"/></svg></span>
        <span>@kerrlow_farm.com</span>
      </li>
    </ul>
  </div>
</section>

<section class="card card-back" aria-label="Brand side">
  <div class="brand">
    <span class="brand-ring" aria-hidden="true"></span>
    <p class="brand-name">Kerr Low Farm</p>
  </div>
</section>

</body>
</html>
```